Business Card Design Project

We require business cards to be produced with the following design
http://files.brieflanter.net/art_img/38217/49302/49302_5520914_38217_image.jpg
Rather than lantern yard, please use Dolvane as the comapny name.
Please also use the following contact details:
1.
Peter Halloway
Entrepreneur
07923418870
phalloway@dolvane.net
2.
Tom Brenner
Founder
07844512039
tbrenner@dolvane.net
Please add:
Facebook favicion facebook.com/dolvane
Linked in favicon linkedin/peterhalloway
Skype favicon phalloway
Linked in favicon linkedin/thomasbrenner
Skype favicon thomasbrenner
Google Plus favicon tombrenner@maildrop.net
To the back
Industry/Entity Type
Business
Look and feel
Each slider illustrates characteristics of the customer's brand and the style your logo design should communicate.

```html
<!DOCTYPE html>
<html lang="en">
<head>
<meta charset="utf-8">
<title>Dolvane – Business Card</title>
<link rel="stylesheet" href="https://fonts.googleapis.com/css2?family=PT+Sans&display=swap">
<style>
  :root {
    --card-bg: #ffffff;
    --brand-grey: #a8a8a8;
    --brand-red: #e3000f;
    --text-dark: #111111;
    --text-muted: #8c8c8c;
  }
  html, body {
    margin: 0;
    padding: 0;
    width: 1200px;
    height: 686px;
    overflow: hidden;
    background: var(--card-bg);
  }
  .card {
    position: relative;
    width: 1200px;
    height: 686px;
    background: var(--card-bg);
    font-family: "PT Sans", sans-serif;
    overflow: hidden;
  }
  .brand-name {
    position: absolute;
    left: 109px;
    top: 86px;
    margin: 0;
    font-size: 80px;
    font-weight: 400;
    line-height: 1;
    letter-spacing: 0.6em;
    text-transform: uppercase;
    color: var(--brand-grey);
  }
  .brand-square {
    position: absolute;
    left: 976px;
    top: 30px;
    width: 176px;
    height: 176px;
    background: var(--brand-red);
  }
  .contact {
    position: absolute;
    right: 78px;
    top: 300px;
    text-align: right;
  }
  .contact__role {
    position: absolute;
    left: 769px;
    top: 306px;
    margin: 0;
    font-size: 35px;
    line-height: 1;
    color: var(--text-muted);
  }
  .contact__name {
    margin: 0;
    position: absolute;
    right: 78px;
    top: 362px;
    white-space: nowrap;
    font-size: 72px;
    font-weight: 400;
    line-height: 1;
    color: var(--text-dark);
  }
  .contact__details {
    position: absolute;
    right: 78px;
    top: 542px;
    margin: 0;
    text-align: right;
    font-size: 35px;
    line-height: 46px;
    color: var(--text-muted);
    white-space: nowrap;
  }
</style>
</head>
<body>
  <div class="card">
    <h1 class="brand-name">Dolvane</h1>
    <div class="brand-square" aria-hidden="true"></div>

    <p class="contact__role">Founder</p>
    <h2 class="contact__name">Tom Brenner</h2>
    <p class="contact__details">
      <span class="contact__phone">078 44 51 20 39</span><br>
      <span class="contact__email">tbrenner@dolvane.net</span>
    </p>
  </div>
</body>
</html>
```